Updated Business Card Re-design (Logo Provided)

I am needing to update our business cards for our practice, Bright Harbor Care. We are a personal injury and wellness practice. The final design should be elegant and classy, but a type of card people would want to keep. Any samples should only have Dr. Tarek Minouvel on the template.
Updates

Went on vacation/holiday

Need extra days to review

Target Market(s)

Personal Injury clients, wellness clients

Industry/Entity Type

Personal Injury, medical, wellness

Contact Information for Business Card

dr and practice name, offerings

Requirements
Must have
• Single sided, this will be printed on a transparent business card, no exceptions.

```html
<!DOCTYPE html>
<html lang="en">
<head>
<meta charset="utf-8">
<title>Bright Harbor Care – Business Card</title>
<link href="https://fonts.googleapis.com/css2?family=Poppins:wght@400;500;600;700&display=swap" rel="stylesheet">
<style>
  :root {
    --brand-blue: #1a74bb;
    --brand-orange: #f2921f;
    --wave-light: #8fd9ee;
    --wave-mid: #3fb6dc;
    --wave-deep: #1d7fa6;
    --paper: #ffffff;
    --ink-dark: #070707;
    --stage: #e7e1d8;
    --canvas: #ffffff;
  }
  * { margin: 0; padding: 0; box-sizing: border-box; }
  html, body { width: 1200px; height: 2379px; overflow: hidden; background: var(--canvas); }
  body { position: relative; font-family: "Poppins", sans-serif; }

  .stage {
    position: absolute; left: 0; top: 0; width: 1200px; height: 868px;
    background: var(--stage);
  }

  .card {
    position: absolute; overflow: hidden; border-radius: 42px;
    background: var(--paper);
    box-shadow: 6px 8px 10px rgba(0,0,0,0.35);
  }
  .card--clear {
    left: 108px; top: 187px; width: 984px; height: 548px;
    background: rgba(255,255,255,0.45);
    border: 1px solid rgba(120,110,100,0.45);
    box-shadow: none;
  }
  .card--white { left: 125px; top: 1015px; width: 952px; height: 545px; }
  .card--black { left: 125px; top: 1657px; width: 952px; height: 545px; background: var(--ink-dark); }

  .brand {
    position: absolute; left: 0; right: 0; top: 86px;
    display: flex; align-items: center; justify-content: center; gap: 18px;
  }
  .brand__dot { width: 54px; height: 54px; border-radius: 50%; background: var(--brand-orange); }
  .brand__name {
    font-weight: 700; font-size: 36px; letter-spacing: -0.5px;
    color: var(--brand-blue); line-height: 1;
  }

  .details { position: absolute; left: 70px; top: 246px; color: var(--brand-blue); }
  .card--clear .details { left: 72px; top: 236px; }
  .details__name { font-weight: 700; font-size: 31px; letter-spacing: -0.6px; line-height: 1.2; }
  .details__role { font-weight: 500; font-size: 12.5px; margin-top: 4px; }
  .details__address { font-size: 20px; line-height: 25px; margin-top: 28px; }
  .contact { list-style: none; font-size: 20.5px; line-height: 30px; margin-top: 4px; }
  .contact li { display: flex; align-items: center; gap: 20px; padding-left: 5px; }
  .contact svg { width: 14px; height: 14px; flex: none; }

  .wave-area {
    position: absolute; right: 0; bottom: 0; width: 430px; height: 245px;
    background: linear-gradient(200deg, rgba(143,217,238,0) 0%, var(--wave-light) 35%, var(--wave-mid) 100%);
  }
  .wave-area--small {
    right: auto; left: 240px; width: 190px; height: 36px;
    background: linear-gradient(180deg, var(--wave-light), var(--wave-mid));
  }
  .card--clear .wave-area {
    width: 440px; height: 245px; opacity: 0.85;
    background: linear-gradient(200deg, rgba(78,174,203,0) 0%, #4eaecb 35%, var(--wave-deep) 100%);
  }
  .card--clear .wave-area--small {
    left: 250px; width: 180px; height: 30px; right: auto;
    background: linear-gradient(180deg, #4eaecb, var(--wave-deep));
  }
</style>
</head>
<body>
  <div class="stage"></div>

  <section class="card card--clear">
    <div class="brand"><span class="brand__dot"></span><span class="brand__name">BRIGHT HARBOR CARE</span></div>
    <div class="wave-area" role="img" aria-label="Flowing blue line-art wave decoration"></div>
    <div class="wave-area wave-area--small" role="img" aria-label="Small blue wave decoration"></div>
    <div class="details">
      <div class="details__name">DR. TAREK MINOUVEL</div>
      <div class="details__role">WELLNESS COACH , CONSULTANT &amp; TRAINER</div>
      <div class="details__address">2140 Marlow Avenue<br>Seabrook, VA 23410</div>
      <ul class="contact">
        <li><svg viewBox="0 0 16 16"><path d="M1 6c0-3 14-3 14 0v2h-4V6H5v2H1z M4 9h8l2 5H2z" fill="#f2921f"/></svg>757-XXX-XXXX</li>
        <li><svg viewBox="0 0 16 16"><circle cx="8" cy="8" r="7" fill="none" stroke="#f2921f" stroke-width="1.6"/><path d="M1 8h14M8 1c-3 4-3 10 0 14M8 1c3 4 3 10 0 14" fill="none" stroke="#f2921f" stroke-width="1.2"/></svg>harborwell.com</li>
        <li><svg viewBox="0 0 16 16"><rect x="1" y="3" width="14" height="10" fill="#f2921f"/><path d="M1 3l7 6 7-6" fill="none" stroke="#fff" stroke-width="1.3"/></svg>info@brightharborcare.com</li>
      </ul>
    </div>
  </section>

  <section class="card card--white">
    <div class="brand"><span class="brand__dot"></span><span class="brand__name">BRIGHT HARBOR CARE</span></div>
    <div class="wave-area" role="img" aria-label="Flowing blue line-art wave decoration"></div>
    <div class="wave-area wave-area--small" role="img" aria-label="Small blue wave decoration"></div>
    <div class="details">
      <div class="details__name">DR. TAREK MINOUVEL</div>
      <div class="details__role">WELLNESS COACH , CONSULTANT &amp; TRAINER</div>
      <div class="details__address">2140 Marlow Avenue<br>Seabrook, VA 23410</div>
      <ul class="contact">
        <li><svg viewBox="0 0 16 16"><path d="M1 6c0-3 14-3 14 0v2h-4V6H5v2H1z M4 9h8l2 5H2z" fill="#f2921f"/></svg>757-XXX-XXXX</li>
        <li><svg viewBox="0 0 16 16"><circle cx="8" cy="8" r="7" fill="none" stroke="#f2921f" stroke-width="1.6"/><path d="M1 8h14M8 1c-3 4-3 10 0 14M8 1c3 4 3 10 0 14" fill="none" stroke="#f2921f" stroke-width="1.2"/></svg>harborwell.com</li>
        <li><svg viewBox="0 0 16 16"><rect x="1" y="3" width="14" height="10" fill="#f2921f"/><path d="M1 3l7 6 7-6" fill="none" stroke="#fff" stroke-width="1.3"/></svg>info@brightharborcare.com</li>
      </ul>
    </div>
  </section>

  <section class="card card--black">
    <div class="brand"><span class="brand__dot"></span><span class="brand__name">BRIGHT HARBOR CARE</span></div>
    <div class="wave-area" role="img" aria-label="Flowing blue line-art wave decoration"></div>
    <div class="wave-area wave-area--small" role="img" aria-label="Small blue wave decoration"></div>
    <div class="details">
      <div class="details__name">DR. TAREK MINOUVEL</div>
      <div class="details__role">WELLNESS COACH , CONSULTANT &amp; TRAINER</div>
      <div class="details__address">2140 Marlow Avenue<br>Seabrook, VA 23410</div>
      <ul class="contact">
        <li><svg viewBox="0 0 16 16"><path d="M1 6c0-3 14-3 14 0v2h-4V6H5v2H1z M4 9h8l2 5H2z" fill="#f2921f"/></svg>757-XXX-XXXX</li>
        <li><svg viewBox="0 0 16 16"><circle cx="8" cy="8" r="7" fill="none" stroke="#f2921f" stroke-width="1.6"/><path d="M1 8h14M8 1c-3 4-3 10 0 14M8 1c3 4 3 10 0 14" fill="none" stroke="#f2921f" stroke-width="1.2"/></svg>harborwell.com</li>
        <li><svg viewBox="0 0 16 16"><rect x="1" y="3" width="14" height="10" fill="#f2921f"/><path d="M1 3l7 6 7-6" fill="none" stroke="#000" stroke-width="1.3"/></svg>info@brightharborcare.com</li>
      </ul>
    </div>
  </section>
</body>
</html>
```